Harbinger Noble Alloys Works Business Cards

We are wanting to have a new business card designed for our company as we go to a convention. We want to balance business/Modern with elegance and beauty. Our company sells highend jewelry pieces. We want to utilize the colors of Black and Gold and have gold foiled fonts to be physically printed on the business cards.
We also would like to have space to write notes on the back side of the business card. When we meet people at jewelry conventions we would like to write notes if possible.
Here are websites and designs that we like the look and feel of these companies and you can use these as design ideas.
https://www.lorvanne.com
https://www.bellquist.com/en-us/home
Here is our company website link
www.harbingernaw.com
I also up loaded two versions of our logo.
- Update 4.26.22
I have uploaded photos of a business card we like. this card has raised embossed letters that you can feel. the raise letters are like a plastic but we don't need to use that...I uploaded to show you that we like the experience of the client feeling the characters of the logo. we also would like to have the material as a satin or some material very soft.
- Maybe we can get designs with beautiful gold foiling and raised characters and logos. we like simplicity...not busy but an elegant design. We need to write notes and would like a section where we can write notes. but we want an elegant style and the client has an experience with the feel of the card when they touch the card.
Colors
- Main colors Black & Gold
- white or light colors for small notes section.
Specialty ideals and things we would like to see based on your design styles.
- raised fonts
- raised logos
- gold foiling
- satin/soft finish on the card material.
we are wanting to design a business card that looks elegant and clean. When the client is handed the business card we want them to physically experience the business card as well by touching the raised logos or fonts and the base material is soft satin. I hope this helps with further designs.
thank you all
We uploaded a new contact layout that we have designed in our office. we would like to see how this would look on your designs.
thank you
I just finished uploading the Contact Layout. the colors are just examples. please use this layout as an idea and use colors based on the feed back we have given each of you personally.
Contact Information for Business Card
we need an area to write notes, we would like to have our logos or the diamond of our logo or the business card to have embossed sections to the business card so when the customer touches the card they can feel the logo. we would also like sections of our business card to have gold foiling. we would also like to use a satin soft paper with our card. when the client touches the card its super soft and high quality
Requirements
Must have
- we would like to have our logos or the diamond of our logo or the business card to have embossed sections to the business card so when the customer touches the card they can feel the logo. we would also like sections of our business card to have gold foiling. we would also like to use a satin soft paper with our card. when the client touches the card its super soft and high quality
Nice to have
- we would like to have our logos or the diamond of our logo or the business card to have embossed sections to the business card so when the customer touches the card they can feel the logo. we would also like sections of our business card to have gold foiling.

```html
<!DOCTYPE html>
<html lang="en">
<head>
<meta charset="utf-8">
<title>Harbinger Noble Alloys Works – Business Card</title>
<link rel="stylesheet" href="https://fonts.googleapis.com/css2?family=Cormorant+SC:wght@500&family=Outfit:wght@600&display=swap">
<style>
  :root {
    --page: #ffffff;
    --ink: #111111;
    --note-line: #333333;
    --paper: #ffffff;
    --gold-deep: #a2601a;
    --gold-mid: #c9881f;
    --gold-bright: #f0bd3a;
    --gold-warm: #dca02c;
    --front-edge: #8a8f99;
    --back-edge: #111111;
  }
  * { box-sizing: border-box; margin: 0; padding: 0; }
  html, body {
    width: 1200px; height: 1180px; overflow: hidden; background: var(--page);
  }
  .sheet { position: relative; width: 1200px; height: 1180px; }
  .card {
    position: absolute; left: 213px; width: 793px; height: 440px;
  }
  .card--front { top: 124px; border: 1px solid var(--front-edge); }
  .card--back { top: 592px; border: 1px solid var(--back-edge); }
  .foil-frame {
    position: absolute; inset: 0;
    background:
      linear-gradient(180deg, rgba(255,214,90,0.35) 0%, rgba(0,0,0,0) 12%, rgba(0,0,0,0) 88%, rgba(120,60,10,0.25) 100%),
      linear-gradient(100deg, var(--gold-mid) 0%, var(--gold-bright) 6%, var(--gold-warm) 14%, var(--gold-mid) 30%, var(--gold-warm) 48%, var(--gold-mid) 62%, var(--gold-bright) 74%, var(--gold-deep) 90%, var(--gold-mid) 100%);
  }
  .paper {
    position: absolute; left: 41px; top: 44px; right: 42px; bottom: 43px;
    background: var(--paper);
  }
  .identity {
    position: absolute; left: 0; right: 0; top: 80px;
    text-align: center; color: var(--ink);
  }
  .brand-name {
    font-family: "Cormorant SC", "Times New Roman", serif;
    font-weight: 500; font-size: 37px; line-height: 1; letter-spacing: 0.2px;
  }
  .tagline {
    margin-top: 6px;
    font-family: "Cormorant SC", "Times New Roman", serif;
    font-weight: 500; font-size: 25px; line-height: 1; letter-spacing: 0.5px;
  }
  .contact {
    position: absolute; left: 0; right: 0; top: 170px;
    text-align: center; color: var(--ink);
    font-family: "Outfit", "Helvetica Neue", Arial, sans-serif;
    font-weight: 600; font-size: 35px; line-height: 1;
  }
  .contact__email { margin-top: 17px; }
  .notes { position: absolute; inset: 0; }
</style>
</head>
<body>
<main class="sheet">
  <section class="card card--front" aria-label="Business card front">
    <div class="foil-frame" role="img" aria-label="Gold foil textured border"></div>
    <div class="paper">
      <div class="identity">
        <p class="brand-name">Harbinger Noble Alloys</p>
        <p class="tagline">– Coins, Jewelry &amp; Diamonds –</p>
      </div>
      <div class="contact">
        <p class="contact__phone">+(555) 014-2287</p>
        <p class="contact__email">info@harbingernaw.com</p>
      </div>
    </div>
  </section>

  <section class="card card--back" aria-label="Business card back with note lines">
    <div class="foil-frame" role="img" aria-label="Gold foil textured border"></div>
    <div class="paper">
      <svg class="notes" width="710" height="353" viewBox="0 0 710 353" aria-hidden="true">
        <g stroke="var(--note-line)" stroke-width="1" stroke-dasharray="6 6.5">
          <line x1="37" y1="53.5" x2="662" y2="53.5"/>
          <line x1="37" y1="116.5" x2="662" y2="116.5"/>
          <line x1="37" y1="178.5" x2="662" y2="178.5"/>
          <line x1="37" y1="240.5" x2="662" y2="240.5"/>
          <line x1="37" y1="302.5" x2="662" y2="302.5"/>
        </g>
      </svg>
    </div>
  </section>
</main>
</body>
</html>
```